Rollup Banner & Flyer für eine Messe "Erfolg durch Innovation"

Wir benötigten für eine Messe einen Roll Up Banner und Flyer zum verteilen. Gerne basierend auf der aktuellen Firmenpräsentation und mit unseren Referenzen.
Im flyer sollen unserer Leistungen (Datenanalyse, Simulation, Optimierung und Webapplikation) dargestellt werden mit einem kleinen Text und einem aussagekräftigen bild. (https://www.kalvento.ch/leistungen/)

Target Market(s)

Industrie

Industry/Entity Type

Simulation

Font styles to use
Sans Serif
Other font styles liked:
• Roboto

Requirements
Must have
• Logo, Referenzen

```html
<!DOCTYPE html>
<html lang="de">
<head>
<meta charset="utf-8">
<title>Kalvento – Leistungen Roll-up</title>
<link rel="stylesheet" href="https://fonts.googleapis.com/css2?family=Roboto:wght@400;500;700&display=swap">
<style>
  :root {
    --stage: #ededed;
    --paper: #ffffff;
    --ink: #111111;
    --text: #333333;
    --lime: #dbe05e;
    --lime-line: #e1e65c;
    --block: #0d0d0d;
    --screen-a: #e9ecef;
    --screen-b: #b9c3cc;
  }
  * { margin: 0; padding: 0; box-sizing: border-box; }
  html, body { width: 1200px; height: 1200px; overflow: hidden; }
  body {
    background: var(--stage);
    font-family: "Roboto", Arial, sans-serif;
    position: relative;
  }
  .rollup {
    position: absolute;
    left: 400px; top: 62px;
    width: 402px; height: 1076px;
    background: var(--paper);
    overflow: hidden;
  }
  .brand {
    position: absolute;
    top: 66px; left: 0; width: 100%;
    text-align: center;
    font-size: 42px; font-weight: 700; line-height: 1;
    color: var(--ink); letter-spacing: 0.5px;
  }
  .hero-visual {
    position: absolute;
    left: 97px; top: 188px;
    width: 205px; height: 200px;
    border-radius: 6px;
    background: linear-gradient(180deg, var(--screen-a), var(--screen-b));
  }
  .headline {
    position: absolute;
    top: 400px; left: 0; width: 100%;
    text-align: center;
    font-size: 64px; font-weight: 700; color: var(--ink);
    letter-spacing: -0.5px; line-height: 1.2;
  }
  .intro {
    position: absolute;
    top: 483px; left: 34px; right: 34px;
    text-align: center;
    font-size: 8.4px; line-height: 1.4; color: var(--text);
  }
  .intro p + p { margin-top: 8px; }
  .service {
    position: absolute; left: 0; width: 100%; height: 110px;
    display: flex;
  }
  .service-icon {
    width: 100px; height: 100%;
    background: var(--block);
    display: flex; align-items: center; justify-content: center;
  }
  .service-icon svg { width: 48px; height: 48px; fill: none; stroke: var(--lime-line); stroke-width: 1.6; stroke-linecap: round; stroke-linejoin: round; }
  .service-body {
    flex: 1; background: var(--lime);
    padding: 12px 14px 0 16px;
  }
  .service-title { font-size: 26px; font-weight: 500; color: var(--ink); line-height: 1.1; }
  .service-text { font-size: 8.4px; line-height: 1.4; color: var(--ink); margin-top: 8px; }
  .s1 { top: 584px; }
  .s2 { top: 703px; }
  .s3 { top: 822px; }
  .s4 { top: 941px; }
</style>
</head>
<body>
  <main class="rollup">
    <header class="brand">Kalvento</header>

    <div class="hero-visual" role="img" aria-label="Bildschirm mit 3D-Simulation einer Lagerhalle"></div>

    <h1 class="headline">Leistungen</h1>

    <div class="intro">
      <p>Mit Simulation, Datenanalyse und Optimierung entwickeln wir Lösungen, die komplexe Prozesse sichtbar machen, Varianten vergleichbar machen und bessere Entscheidungen ermöglichen.</p>
      <p>Wir begleiten unsere Kunden vom schnellen Vorprojekt bis zur produktiven Lösung – pragmatisch, technisch stark und immer mit Fokus auf dem Nutzen.</p>
    </div>

    <section class="service s1">
      <div class="service-icon">
        <svg viewBox="0 0 48 48">
          <ellipse cx="24" cy="17" rx="7" ry="3"/>
          <path d="M17 17v14c0 1.7 3.1 3 7 3s7-1.3 7-3V17"/>
          <path d="M17 24c0 1.7 3.1 3 7 3s7-1.3 7-3"/>
          <ellipse cx="24" cy="24" rx="21" ry="9" transform="rotate(-35 24 24)"/>
          <ellipse cx="24" cy="24" rx="21" ry="9" transform="rotate(35 24 24)"/>
        </svg>
      </div>
      <div class="service-body">
        <h2 class="service-title">Datenanalyse</h2>
        <p class="service-text">Datenanalyse macht Prozesse sichtbar, erkennt Muster und schafft eine objektive Grundlage für Entscheidungen. Wir strukturieren, bereinigen und analysieren Daten so, dass sie einen echten Nutzen erzeugen.</p>
      </div>
    </section>

    <section class="service s2">
      <div class="service-icon">
        <svg viewBox="0 0 48 48">
          <rect x="5" y="8" width="38" height="27" rx="2"/>
          <path d="M18 35v5M30 35v5M14 40h20"/>
          <path d="M9 18h5l2-4 3 8 2-4h6"/>
          <rect x="9" y="25" width="6" height="6"/>
          <rect x="18" y="25" width="6" height="6"/>
          <rect x="27" y="25" width="6" height="6"/>
          <path d="M34 13h5M34 18h5M34 23h5"/>
        </svg>
      </div>
      <div class="service-body">
        <h2 class="service-title">Simulation</h2>
        <p class="service-text">Simulation bildet reale Prozesse digital ab, damit Abläufe, Kapazitäten und Varianten risikofrei getestet werden können.</p>
      </div>
    </section>

    <section class="service s3">
      <div class="service-icon">
        <svg viewBox="0 0 48 48">
          <rect x="18" y="4" width="12" height="10"/>
          <path d="M24 14v8M10 22h28M10 22v5M38 22v5"/>
          <rect x="4" y="27" width="12" height="9"/>
          <rect x="32" y="27" width="12" height="9"/>
          <circle cx="24" cy="32" r="4"/>
          <path d="M24 26v2M24 36v2M18 32h2M28 32h2"/>
          <path d="M10 36v6h28v-6"/>
        </svg>
      </div>
      <div class="service-body">
        <h2 class="service-title">Optimierung</h2>
        <p class="service-text">Optimierung sucht automatisch nach der besten Lösung – sei es bei Planung, Ressourcen, Routen oder Abläufen. Mit Algorithmen und intelligenten Modellen finden wir Varianten, die Kosten senken, Kapazitäten besser nutzen und Entscheidungen beschleunigen.</p>
      </div>
    </section>

    <section class="service s4">
      <div class="service-icon">
        <svg viewBox="0 0 48 48">
          <rect x="5" y="7" width="38" height="28" rx="2"/>
          <path d="M18 35v5M30 35v5M14 40h20"/>
          <path d="M9 12h30"/>
          <rect x="11" y="17" width="20" height="10"/>
          <path d="M28 23l8 3-3 1 2 4-2 1-2-4-3 2z"/>
        </svg>
      </div>
      <div class="service-body">
        <h2 class="service-title">Webapplikationen</h2>
        <p class="service-text">Wir entwickeln individuelle Webapplikationen, die Daten, Simulationen und Optimierungen in einem benutzerfreundlichen Tool zusammenführen. So entstehen Lösungen, die direkt im Alltag genutzt werden – einfach, schnell und ohne Installation.</p>
      </div>
    </section>
  </main>
</body>
</html>
```